TrovaLine.com Business Cards

Logo is attached but does not need to be used. We would prefer if the logo was just on the back of the card. We would like something creative for the front of the card.
Please see our website @ www.TrovaLine.com to get a better feel for our company.

Card should include
Name
Title
Phone #
Email Address
Address
Website

Industry/Entity Type

Events

```html
<!DOCTYPE html>
<html lang="en">
<head>
<meta charset="utf-8">
<title>TrovaLine Business Card</title>
<link rel="stylesheet" href="https://fonts.googleapis.com/css2?family=Noto+Sans:wght@400;700&family=Audiowide&family=Oswald:wght@300&family=Kalam&display=swap">
<style>
  :root {
    --page: #ffffff;
    --card: #000000;
    --band: #2a0a08;
    --ink: #ffffff;
    --accent-red: #e8110f;
    --swirl-green: #1faa35;
    --swirl-dark: #0a3a12;
  }
  * { margin: 0; padding: 0; box-sizing: border-box; }
  html, body {
    width: 1200px;
    height: 720px;
    overflow: hidden;
    background: var(--page);
  }
  .card {
    position: absolute;
    left: 40px;
    top: 40px;
    width: 1120px;
    height: 640px;
    background:
      linear-gradient(to bottom,
        var(--card) 0%,
        var(--card) 20%,
        var(--band) 42%,
        var(--band) 58%,
        var(--card) 80%,
        var(--card) 100%);
    overflow: hidden;
  }
  .holder-name {
    position: absolute;
    left: 21px;
    top: 18px;
    font-family: "Noto Sans", sans-serif;
    font-size: 33px;
    line-height: 1.2;
    color: var(--ink);
  }
  .website {
    position: absolute;
    right: 22px;
    top: 20px;
    font-family: "Noto Sans", sans-serif;
    font-weight: 700;
    font-size: 30px;
    line-height: 1.2;
    color: var(--accent-red);
  }
  .flourish {
    position: absolute;
    top: 173px;
    width: 300px;
    height: 300px;
    background: radial-gradient(ellipse at center,
      rgba(31,170,53,0.55) 0%,
      rgba(10,58,18,0.4) 45%,
      rgba(0,0,0,0) 72%);
  }
  .flourish--left { left: 30px; }
  .flourish--right { left: 750px; }
  .job-title {
    position: absolute;
    left: 0;
    right: 0;
    top: 276px;
    text-align center;
    text-align: center;
    font-family: "Audiowide", sans-serif;
    font-weight: 400;
    font-size: 60px;
    letter-spacing: 3px;
    line-height: 1.1;
    color: var(--ink);
  }
  .title-rule {
    position: absolute;
    top: 365px;
    height: 2px;
    background: var(--swirl-green);
  }
  .title-rule--left { left: 300px; width: 157px; }
  .title-rule--right { left: 642px; width: 160px; }
  .phone {
    position: absolute;
    left: 0;
    right: 0;
    top: 362px;
    text-align: center;
    font-family: "Oswald", sans-serif;
    font-weight: 300;
    font-size: 62px;
    line-height: 1.1;
    color: var(--ink);
  }
  .contact-line {
    position: absolute;
    left: 0;
    right: 0;
    top: 576px;
    text-align: center;
    font-family: "Kalam", cursive;
    font-size: 33px;
    line-height: 1.2;
    color: var(--ink);
    white-space: nowrap;
  }
</style>
</head>
<body>
  <main class="card">
    <p class="holder-name">Leo Marsh</p>
    <p class="website">www.TrovaLine.com</p>

    <div class="flourish flourish--left" role="img" aria-label="Green fractal swirl ornament"></div>
    <div class="flourish flourish--right" role="img" aria-label="Green fractal swirl ornament, mirrored"></div>

    <h1 class="job-title">Web Designer</h1>
    <div class="title-rule title-rule--left"></div>
    <div class="title-rule title-rule--right"></div>
    <p class="phone">555 - 230 - 4187</p>

    <p class="contact-line">leo.marsh@trovaline.com, 214, 18th St, Suite No.07, Brookfield, NY - 10021</p>
  </main>
</body>
</html>
```